New webpage design for Talvora.se, participant management system informationpage.

Project Brief: New Website Design for Talvora.se (Participant Management System)
About Talvora.se:
Talvora.se is an established participant management system used by organizations and course providers in Sweden to handle event and course registrations. Our website’s primary audience is course providers, event organizers, and potential users seeking efficient management tools.
Project Goal:
We are launching a new public-facing website for Talvora.se, which will present information about our system, features, FAQ, pricing, news, testimonials, and more. The new site will be built in Umbraco CMS and should follow our visual identity as described in the attached graphic manual.
Deliverables:
We need complete, modern, and responsive page designs (desktop and mobile) for the following pages:
- Home page (landing page)
- Features page
- FAQ page
- About Us page
- Contact Us / Book a Demo page
- Pricing page
- Testimonials page
- News / Blog page
Design Guidelines:
- Please use the attached Plomvik graphic manual for guidance (Plomvik is a sister project; use the same branding).
- The Talvora.se logo is attached and must be included.
- Please use the blue color palette variant from the guide.
- Typography and graphic elements should be consistent with the manual.
- Designs must be suitable for implementation in Umbraco CMS (avoid overly complex layouts or animations that might be difficult to develop).
- All designs should be responsive and work well on desktop, tablet, and mobile.
- Final deliverables should be provided in Figma or Adobe XD (preferably Figma).
What We Like:
- Clean, modern, Scandinavian style.
- Clear navigation and strong hierarchy.
- Readable, accessible layouts.
What to Avoid:
- Overly playful or cartoonish elements.
- Too much clutter or excessive graphical elements.
- Dark color schemes (please focus on blue/light).
References:
- Our current site: https://talvora-demo.se
- Graphic manual (see attachment)
- Talvora logo (see attachment)
Additional Notes:
- The new design should improve clarity, usability, and visual appeal compared to our current site.
- Feel free to suggest visual improvements, but remain consistent with our brand guidelines.
Other font styles liked:
- Orev and Cabin. See attached font files

```html
<!DOCTYPE html>
<html lang="en">
<head>
<meta charset="utf-8">
<title>About Us – Talvora</title>
<link href="https://fonts.googleapis.com/css2?family=Cabin:wght@400;500&family=Lato:wght@400;700&display=swap" rel="stylesheet">
<style>
:root{
  --ink:#111417;
  --text:#333a40;
  --teal:#219a8b;
  --teal-dark:#16897b;
  --pink:#ea2a6d;
  --soft:#f6f6fb;
  --line:#d9dde0;
  --white:#ffffff;
}
*{box-sizing:border-box;margin:0;padding:0}
html,body{width:1200px;height:2521px;overflow:hidden}
body{position:relative;font-family:"Lato",sans-serif;color:var(--text);background:var(--white)}
.abs{position:absolute}
.hero-bg{left:0;top:0;width:1200px;height:1069px;
  background:
   radial-gradient(circle at 45% 8%, rgba(205,200,255,.55), transparent 22%),
   radial-gradient(circle at 95% 12%, rgba(160,245,225,.7), transparent 30%),
   radial-gradient(circle at 3% 5%, rgba(230,245,190,.7), transparent 25%),
   radial-gradient(circle at 8% 35%, rgba(225,190,250,.6), transparent 25%),
   radial-gradient(circle at 70% 42%, rgba(250,190,240,.55), transparent 20%),
   radial-gradient(circle at 90% 40%, rgba(160,225,250,.6), transparent 25%),
   #fff;}
.brand{font-family:"Cabin",sans-serif;font-weight:400;color:var(--ink);letter-spacing:1px}
.nav{top:34px;left:376px;display:flex;gap:29px;font-size:13px;color:var(--ink);align-items:center}
.nav .active{color:var(--teal);font-weight:700}
.btn{display:flex;align-items:center;justify-content:center;font-size:13px;border-radius:3px}
.btn-outline{border:1px solid var(--teal);color:var(--ink);background:rgba(255,255,255,.3)}
.btn-primary{background:var(--pink);color:var(--white)}
h1,h2,h3{font-family:"Cabin",sans-serif;font-weight:500;color:var(--ink)}
.page-title{top:146px;width:1200px;text-align:center;font-size:37px}
.photo{border-radius:50%}
.sec-title{font-size:35px}
.copy{font-size:13px;line-height:18.8px;color:var(--text)}
.band-soft{left:0;top:1069px;width:1200px;height:353px;background:var(--soft)}
.ticks{list-style:none;font-size:13px}
.ticks li{display:flex;align-items:center;gap:9px;height:37px}
.cta{left:0;top:1936px;width:1200px;height:186px;background:var(--teal)}
.cta h2{color:var(--white);font-size:36px}
.foot-h{font-size:21px}
.links{list-style:none;font-size:13px;line-height:18.8px;color:var(--ink)}
.social{width:22px;height:22px;border-radius:50%}
</style>
</head>
<body>
<div class="abs hero-bg"></div>

<header>
  <div class="abs brand" style="left:113px;top:26px;font-size:34px">talvora.</div>
  <nav class="abs nav">
    <svg width="15" height="13" viewBox="0 0 15 13"><path d="M7.5 0 0 6.5h2V13h4V9h3v4h4V6.5h2z" fill="#111417"/></svg>
    <span>Features</span><span>Pricing</span><span>FAQ</span><span>Testimonials</span><span>News</span><span class="active">About</span>
  </nav>
  <div class="abs btn btn-outline" style="left:884px;top:30px;width:103px;height:33px">Contact us</div>
  <div class="abs btn btn-primary" style="left:991px;top:31px;width:102px;height:32px">Book a Demo</div>
</header>

<main>
  <h1 class="abs page-title">About Us – Talvora</h1>

  <div class="abs photo" role="img" aria-label="Photo of historic orange and red buildings in Stockholm at sunset" style="left:198px;top:266px;width:378px;height:378px;background:linear-gradient(160deg,#f4b387 0%,#c8694a 40%,#8a4b3c 65%,#4f6b34 100%)"></div>
  <h2 class="abs sec-title" style="left:628px;top:344px">Who We Are</h2>
  <p class="abs copy" style="left:628px;top:404px;width:378px">Talvora.se is a trusted participant management system used by event organizers, course providers, and organizations across Sweden. We help you simplify registrations, payments, and communication so you can focus on delivering outstanding experiences. With secure, reliable, and user-friendly tools, Talvora.se adapts to events of any size – from small workshops to large conferences – making event management easier, faster, and more efficient.</p>

  <h2 class="abs sec-title" style="left:199px;top:726px">Our Story</h2>
  <p class="abs copy" style="left:199px;top:786px;width:365px">What started as a small initiative to provide focused, high-quality courses has now evolved into a full-fledged learning ecosystem. At Talvora, we believe that education is not just about information – it's about transformation. We are passionate about helping our learners turn knowledge into action, whether for personal growth, professional development, or exploring new passions.</p>
  <div class="abs photo" role="img" aria-label="Photo of two business colleagues looking at a tablet together" style="left:623px;top:616px;width:380px;height:380px;background:linear-gradient(120deg,#c9cdd2 0%,#9b6a45 35%,#2b2c33 70%,#5e6168 100%)"></div>

  <div class="abs band-soft"></div>
  <h2 class="abs sec-title" style="left:199px;top:1154px">Our Mission</h2>
  <p class="abs copy" style="left:199px;top:1214px;width:380px">Our mission is to create a learning platform that is inspiring, accessible, and effective for everyone. We strive to deliver high-quality courses designed by experts, provide a seamless and intuitive learning experience, support lifelong personal and professional growth, and foster a community where learners motivate and inspire each other to achieve their full potential.</p>
  <h2 class="abs sec-title" style="left:628px;top:1154px">Our Vision</h2>
  <p class="abs copy" style="left:628px;top:1214px;width:380px">Our vision is to create a learning platform that is inspiring, accessible, and effective for everyone. We strive to provide high-quality courses designed by experts, offer a seamless and intuitive learning experience, support lifelong personal and professional growth, and foster a community where learners motivate and inspire each other to achieve their full potential.</p>

  <div class="abs photo" role="img" aria-label="Photo of three students working together on a laptop in a library" style="left:180px;top:1491px;width:380px;height:380px;background:linear-gradient(140deg,#6b4a36 0%,#b9b6b2 35%,#3b4b6a 60%,#1f9a5e 85%,#c9a27a 100%)"></div>
  <h2 class="abs sec-title" style="left:613px;top:1572px">Why Choose Talvora?</h2>
  <ul class="abs ticks" style="left:613px;top:1623px">
    <li><svg width="12" height="12" viewBox="0 0 12 12"><circle cx="6" cy="6" r="6" fill="#111417"/><path d="M3.2 6.2 5.2 8 8.9 4.2" stroke="#fff" stroke-width="1.6" fill="none"/></svg>Expert-designed courses for real-world skills</li>
    <li><svg width="12" height="12" viewBox="0 0 12 12"><circle cx="6" cy="6" r="6" fill="#111417"/><path d="M3.2 6.2 5.2 8 8.9 4.2" stroke="#fff" stroke-width="1.6" fill="none"/></svg>Interactive and engaging learning formats</li>
    <li><svg width="12" height="12" viewBox="0 0 12 12"><circle cx="6" cy="6" r="6" fill="#111417"/><path d="M3.2 6.2 5.2 8 8.9 4.2" stroke="#fff" stroke-width="1.6" fill="none"/></svg>Supportive community of learners and mentors</li>
    <li><svg width="12" height="12" viewBox="0 0 12 12"><circle cx="6" cy="6" r="6" fill="#111417"/><path d="M3.2 6.2 5.2 8 8.9 4.2" stroke="#fff" stroke-width="1.6" fill="none"/></svg>Continuous updates and innovations to improve your learning experience</li>
  </ul>

  <section class="abs cta">
    <h2 class="abs" style="left:137px;top:62px">Want to see Talvora in</h2>
    <p class="abs" style="left:137px;top:110px;font-size:13px;color:#fff">Book a personalised demo – we will walk you through the platform and answer your questions.</p>
    <div class="abs btn" style="left:960px;top:78px;width:111px;height:31px;background:#fff;color:var(--ink)">Book a demo</div>
  </section>
</main>

<footer>
  <div class="abs brand" style="left:155px;top:2214px;font-size:58px">talvora.</div>
  <p class="abs" style="left:146px;top:2295px;width:220px;text-align:center;font-size:13px;line-height:18.8px;color:var(--ink)">Talvora is a participant management platform for course providers and event organisers in Sweden.</p>

  <h3 class="abs foot-h" style="left:475px;top:2196px">Useful Links</h3>
  <ul class="abs links" style="left:478px;top:2232px">
    <li>Home</li><li>Features</li><li>FAQ</li><li>About Us</li><li>Contact Us</li><li>Pricing</li><li>Testimonials</li><li>News</li>
  </ul>

  <h3 class="abs foot-h" style="left:674px;top:2196px">Newsleter</h3>
  <p class="abs" style="left:674px;top:2236px;font-size:12px;color:var(--ink)">Subscribe To Our Newsletter</p>
  <div class="abs" style="left:675px;top:2265px;width:187px;height:32px;border:1px solid var(--line);border-radius:4px;background:#fff"></div>
  <span class="abs" style="left:692px;top:2275px;font-size:10px;color:var(--text)">Email Address</span>
  <svg class="abs" style="left:838px;top:2276px" width="12" height="11" viewBox="0 0 12 11"><path d="M0 5 12 0 9 11 6 7z" fill="#219a8b"/></svg>

  <h3 class="abs foot-h" style="left:944px;top:2196px">Contact Us</h3>
  <div class="abs" style="left:944px;top:2238px;display:flex;align-items:center;gap:6px;font-size:15px;color:var(--ink)">
    <svg width="13" height="13" viewBox="0 0 13 13"><path d="M3 0 5 3 3.8 4.7c.9 2 2.5 3.6 4.5 4.5L10 8l3 2-1 2.5C6 13 0 7 .5 1z" fill="#219a8b"/></svg>010-555 12 34</div>
  <div class="abs" style="left:944px;top:2259px;display:flex;align-items:center;gap:6px;font-size:15px;color:var(--ink)">
    <svg width="13" height="10" viewBox="0 0 13 10"><rect width="13" height="10" rx="1" fill="#219a8b"/><path d="M0 1 6.5 6 13 1" stroke="#fff" fill="none"/></svg>support@talvora.se</div>
  <div class="abs social" style="left:942px;top:2291px;background:#3b5998"></div>
  <div class="abs social" style="left:970px;top:2291px;background:#1da1f2"></div>
  <div class="abs social" style="left:997px;top:2291px;background:#0e5a9a"></div>
  <div class="abs social" style="left:1025px;top:2291px;background:#d6307c"></div>

  <div class="abs" style="left:1125px;top:2445px;width:34px;height:34px;border-radius:50%;background:var(--teal)"></div>
  <svg class="abs" style="left:1138px;top:2458px" width="8" height="6" viewBox="0 0 8 6"><path d="M1 5 4 2 7 5" stroke="#fff" stroke-width="1.4" fill="none"/></svg>

  <div class="abs" style="left:94px;top:2464px;width:1012px;height:2px;background:var(--line)"></div>
  <p class="abs" style="left:94px;top:2486px;font-size:12px;color:var(--ink)">© Talvora 2025 – All rights reserved</p>
  <p class="abs" style="left:1024px;top:2486px;font-size:12px;color:var(--ink)">Privacy • Terms</p>
</footer>
</body>
</html>
```